Yoga Studio needs a new website

I am looking for someone to design a landing/home page for my website. The website will be developed using Wordpress, so please make sure your designs are compatible.

Please note the following design guidelines about the page:
1. The website is for a yoga studio called “Mirel Yoga”. The logo for our studio has been uploaded on along with this project. Mirel in Sanskrit means Truth and Yoga means unity or unification (with supreme consciousness).
2. The Yoga studio will probably the first of its kinda to offer true, authentic, spiritual experience to students in South Africa. More than that, it aims to setup itself as a hub for spiritualists and seekers irrespective of beliefs, religion and what philosophies they subscribe to.
3. Unlike modern schools, this school focuses on true elements of yoga - and teaches Yoga the way it was meant to be - no westernisation. Must have a peaceful, clam, very clean and spiritual look.
4. Please pay careful attention to the logo, color schemes and the simple design. The site must reflect exactly the same principles.
5. Please use the latest web design trends and ideas in your design. You are free to be as creative as you want.
6. You are free to combine or use design concepts from other philosophies such as Sufism, Bahai, Tantra, Buddhism etc. as long as it gels well with the Yoga theme.
7. The overall site should give a very sensual, feminine and very mystic feel.

Functionality, features and guidelines for the main page design:
1. The main page should give a very clean, expansive, clutter free look.
2. The designer should find a clean way to fit all the following links/information into a main page. First prize if the designer could fit everything in a “single screen” - no scrolling.
3. Visually, the following information must be presented on the main page:
1. The name/logo of the studio.
2. The following sections of the website should have a link on the main page. Sub items represent sub sections within a section.
1. Home - Redirects the user back to home page
2. About
1. Mirel Yoga
2. Instructors
3. FAQ
3. Private Sessions
4. Corporate
1. At Workplace
2. Offisite & Team Building
3. Specialized
5. Retreats
6. Therapy
1. Stress & Anxiety
2. Lifestyle Diseases
3. Rehabilitation
4. Others
7. Gallery
8. Contact Us
3. A Calendar for classes and events
4. A section to display latest blog articles with option to share on social media sites.
5. A separate section to display latest news items.
6. A section for photo gallery - the gallery can be categorised in albums. The main page can display a limited number of images and clicking on the image should take user to our flicker account.
7. Lastly, a nice and clean way to show our activity on various social media streams such as facebook, twitter, flickr, Facebook page, google plus etc.

Please do not limit yourself to the brief above. If you any creative ideas or concepts, please feel free to experiment and suggest new features. Use you full creativity.
Updates

Hi, Thank you for all the designs so far and for your hard work. Just wanted to let you know that you can also include design elements from other philosophies as well if you want to such as Sufism, Bahai, Tantra, Buddhism etc. as long as it gels well with the over all Yoga theme. Please also note that the final design have a mystic, feminine and sensual feel to it. Please also try and include/match the logo styles in the design as well. The site should look very premium, very exclusive - just like the logo.

Target Market(s)

the site is being designed for serious yoga practitioners and learners in the age group of 18-45

Industry/Entity Type

School

Requirements
Must have
• clean, expansive, elegant, simple, calming, soothing, peaceful

```html
<!DOCTYPE html>
<html lang="en">
<head>
<meta charset="utf-8">
<title>Mirel Yoga</title>
<link rel="stylesheet" href="https://fonts.googleapis.com/css2?family=Figtree:wght@400;500;600&family=Ropa+Sans&family=Signika:wght@400;500&display=swap">
<style>
:root{
  --blue-deep:#1e3d96;
  --blue-mid:#2a6fc4;
  --ink:#3c3c3c;
  --muted:#6a6a6a;
  --rule:#e3e3e3;
  --footer:#232323;
  --footer-base:#161616;
  --footer-text:#9a9a9a;
  --white:#ffffff;
}
*{margin:0;padding:0;box-sizing:border-box}
html,body{width:1048px;height:1200px;overflow:hidden;background:#f2f2f2}
.canvas{width:1048px;height:1200px;overflow:hidden;position:relative}
.page{width:1200px;height:1374px;position:absolute;left:0;top:0;transform:scale(.873333);transform-origin:0 0;font-family:"Figtree",sans-serif;color:var(--ink);background:linear-gradient(135deg,#f6f6f6,#ececec 40%,#f7f7f7 70%,#eaeaea)}
.abs{position:absolute}

/* header */
.topline{left:0;top:0;width:1200px;height:4px;background:var(--blue-deep)}
.header{left:0;top:4px;width:1200px;height:133px;background:linear-gradient(120deg,#fff 0%,#f4f4f4 35%,#fff 55%,#efefef 80%,#fafafa)}
.quote-btn{left:912px;top:4px;width:178px;height:39px;background:var(--blue-deep);color:#fff;font:600 17px/39px "Figtree",sans-serif;text-align:center}
.contact-row{left:772px;top:82px;display:flex;align-items:center;gap:10px}
.contact-row .phone{color:var(--blue-deep);font:500 16px "Figtree",sans-serif}
.ring{width:28px;height:28px;border:2px solid #222;border-radius:50%;display:flex;align-items:center;justify-content:center}
.social-top{left:942px;top:82px;display:flex;gap:12px}
.logo-box{left:111px;top:0;width:227px;height:212px;background:#fff;box-shadow:0 2px 6px rgba(0,0,0,.12);display:flex;flex-direction:column;align-items:center;justify-content:center;gap:14px;z-index:3}
.logo-mark{width:46px;height:46px;border-radius:50%;background:var(--blue-mid)}
.logo-name{font:600 30px "Figtree",sans-serif;color:var(--blue-deep)}

/* nav */
.nav{left:0;top:137px;width:1200px;height:41px;background:linear-gradient(#3a8ad8,#1f62b8)}
.nav ul{list-style:none;position:absolute;left:389px;top:0;display:flex;height:41px}
.nav li{font:400 17px/41px "Signika",sans-serif;color:#fff;padding:0 17px}
.nav li.active{background:#1c4fa0}

/* hero */
.hero{left:0;top:178px;width:1200px;height:430px;background:radial-gradient(circle at 840px 210px,#5a4031 0 70px,transparent 190px),linear-gradient(180deg,#2d4a22 0%,#5c7a3a 35%,#3e6a2a 70%,#5fa236 100%)}
.hero-title{left:112px;top:250px;font:400 64px/1 "Ropa Sans",sans-serif;color:#fff}
.hero-name{left:112px;top:326px;font:600 56px/1 "Figtree",sans-serif;color:#fff}
.hero-sub{left:111px;top:402px;font:400 19px "Signika",sans-serif;color:#fff}
.btn{height:47px;font:400 20px/45px "Signika",sans-serif;color:#fff;text-align:center;border-radius:3px}
.btn-learn{left:110px;top:453px;width:135px;background:linear-gradient(#2c7fd4,#1b5fb3)}
.btn-class{left:267px;top:452px;width:137px;border:2px solid #fff}

/* content */
.panel{left:90px;top:556px;width:1020px;height:501px;background:#fff}
.col-head{top:578px;height:46px;display:flex;align-items:center;background:linear-gradient(90deg,#8a8a8a,#5a5a5a)}
.col-head .badge{width:46px;height:46px;background:var(--blue-mid);clip-path:polygon(0 0,80% 0,100% 50%,80% 100%,0 100%);display:flex;align-items:center;padding-left:10px}
.col-head h2{font:500 18px "Figtree",sans-serif;color:#fff;margin-left:24px}
.intro{left:111px;top:636px;width:296px;font:400 13.5px/20px "Figtree",sans-serif;color:var(--muted);hyphens:auto}
.about-list{left:111px;top:686px;width:308px;list-style:none}
.about-list li{height:51px;margin-bottom:6px;background:linear-gradient(90deg,#f1f1f1,#fff);display:flex;align-items:center;font:400 15.5px "Figtree",sans-serif;color:#444}
.about-list .arrow{width:15px;height:15px;border-radius:50%;background:#fff;margin:0 24px 0 12px;display:flex;align-items:center;justify-content:center}
.why-list{left:441px;top:650px;width:305px;list-style:none}
.why-list li{display:flex;gap:10px;font:400 13.5px/20px "Figtree",sans-serif;color:var(--muted);padding-bottom:14px;margin-bottom:14px;border-bottom:1px solid var(--rule)}
.why-list li:last-child{border:0;line-height:28px}
.why-list .num{font-weight:600;font-size:16px;color:#666;min-width:18px}
.news{left:774px;top:656px;width:320px;list-style:none}
.news li{display:flex;gap:9px;height:89px}
.thumb{width:64px;height:58px;border:2px solid #333;flex:none}
.news p{font:400 13px/20px "Figtree",sans-serif;color:var(--muted);hyphens:auto}
.stats{display:flex;gap:16px;font:400 12.5px "Figtree",sans-serif;color:#333;margin-top:3px;align-items:center}
.stats span{display:flex;align-items:center;gap:5px}

/* footer */
.band{left:0;top:1057px;width:1200px;height:55px;background:var(--blue-deep)}
.band-btn{left:140px;top:1066px;width:164px;height:38px;background:#222;color:#fff;font:500 14.5px/38px "Figtree",sans-serif;text-align:center;border-radius:2px}
.band-social{left:915px;top:1072px;display:flex;gap:11px}
.band-social span{width:28px;height:28px;border-radius:50%;background:linear-gradient(#f4f4f4,#c8c8c8);display:flex;align-items:center;justify-content:center}
.footer{left:0;top:1112px;width:1200px;height:210px;background:var(--footer)}
.corner{left:0;top:1112px;width:35px;height:25px;background:var(--blue-deep);clip-path:polygon(0 0,100% 0,0 100%)}
.fcol{top:1146px}
.fcol h3{font:400 15px "Figtree",sans-serif;color:#fff;margin-bottom:22px}
.fcol li{list-style:none;font:400 12.5px/20px "Figtree",sans-serif;color:var(--footer-text)}
.addr{display:flex;gap:8px;font:400 12.5px/20px "Figtree",sans-serif;color:var(--footer-text)}
.base{left:0;top:1322px;width:1200px;height:52px;background:var(--footer-base);color:#fff;font:400 13px/52px "Signika",sans-serif;text-align:center}
</style>
</head>
<body>
<div class="canvas">
<div class="page">
  <div class="abs header"></div>
  <div class="abs topline"></div>
  <div class="abs quote-btn">Request a Qoute</div>
  <div class="abs contact-row">
    <span class="ring"><svg width="16" height="16" viewBox="0 0 16 16"><path d="M3 2l3 0 1 3-2 1.5c1 2 2.5 3.5 4.5 4.5L11 9l3 1v3c-6 .5-11.5-5-11-11z" fill="#222"/></svg></span>
    <span class="phone">0144-220-5310</span>
  </div>
  <div class="abs social-top">
    <span class="ring"></span>
    <span class="ring"></span>
    <span class="ring"><svg width="14" height="10" viewBox="0 0 14 10"><rect x="0.5" y="0.5" width="13" height="9" fill="#222"/><path d="M1 1l6 5 6-5" stroke="#fff" fill="none"/></svg></span>
    <span class="ring"></span>
  </div>

  <nav class="abs nav">
    <ul>
      <li class="active">Home</li><li>About us</li><li>Corporate</li><li>Mirel</li><li style="padding:0 23px">Retreats</li><li>Therapy</li><li>Faq's</li><li>Contact Us</li>
    </ul>
  </nav>

  <div class="abs logo-box">
    <span class="logo-mark"></span>
    <span class="logo-name">Mirel Yoga</span>
  </div>

  <div class="abs hero" role="img" aria-label="Photo of a woman meditating cross-legged on grass in a green park"></div>
  <h1 class="abs hero-title">Welcome To</h1>
  <div class="abs hero-name">Mirel Yoga</div>
  <p class="abs hero-sub">Mirel Yoga is our concept of complete wellness.</p>
  <a class="abs btn btn-learn">Learn More</a>
  <a class="abs btn btn-class">Take class</a>

  <div class="abs panel"></div>

  <div class="abs col-head" style="left:110px;width:320px">
    <span class="badge"><svg width="24" height="24" viewBox="0 0 24 24"><path d="M4 4l16 16M20 4L4 20" stroke="#fff" stroke-width="3"/></svg></span><h2>About Us</h2>
  </div>
  <div class="abs col-head" style="left:441px;width:320px">
    <span class="badge"><svg width="24" height="24" viewBox="0 0 24 24"><path d="M4 12l6 6 10-12" stroke="#fff" stroke-width="3.5" fill="none"/></svg></span><h2>Why Us</h2>
  </div>
  <div class="abs col-head" style="left:774px;width:316px">
    <span class="badge"><svg width="24" height="24" viewBox="0 0 24 24"><rect x="3" y="3" width="18" height="18" fill="none" stroke="#fff" stroke-width="2"/><path d="M7 8h10M7 12h10M7 16h10" stroke="#fff" stroke-width="2"/></svg></span><h2>Mirel News</h2>
  </div>

  <p class="abs intro">Lorem ipsum dolor sit amet, consectetur adipiscing elit. Maecenas...</p>
  <ul class="abs about-list">
    <li><span class="arrow"><svg width="6" height="8"><path d="M1 1l4 3-4 3" stroke="#333" fill="none" stroke-width="1.5"/></svg></span>Lorem Ipsum</li>
    <li><span class="arrow"><svg width="6" height="8"><path d="M1 1l4 3-4 3" stroke="#333" fill="none" stroke-width="1.5"/></svg></span>Dolor Sit Amet</li>
    <li><span class="arrow"><svg width="6" height="8"><path d="M1 1l4 3-4 3" stroke="#333" fill="none" stroke-width="1.5"/></svg></span>Consectutuer</li>
    <li><span class="arrow"><svg width="6" height="8"><path d="M1 1l4 3-4 3" stroke="#333" fill="none" stroke-width="1.5"/></svg></span>Adipicsing Diam</li>
    <li><span class="arrow"><svg width="6" height="8"><path d="M1 1l4 3-4 3" stroke="#333" fill="none" stroke-width="1.5"/></svg></span>Set Nonummy Elite</li>
    <li><span class="arrow"><svg width="6" height="8"><path d="M1 1l4 3-4 3" stroke="#333" fill="none" stroke-width="1.5"/></svg></span>Consectutuer Amet</li>
  </ul>

  <ol class="abs why-list">
    <li><span class="num">1.</span><span>Lorem ipsum dolor sit amet, consectetur adipiscing elit. Maecenas nulla ante, ullamcorper vel consectetur vel, tincidunt eget neque. Fusce scelerisque mauris...</span></li>
    <li><span class="num">2.</span><span>et neque ultricies, et egestas elit malesuada. Nulla porta accumsan lobortis. Maecenas purus elit, pulvinar at lectus non...</span></li>
    <li><span class="num">3.</span><span>aliquam tincidunt neque. Quisque pretium eget arcu vel semper. Duis pellentesque, lorem eget fermentum aliquam, neque ex rutrum ipsum, eu varius tellus elit vitae dui.</span></li>
  </ol>

  <ul class="abs news">
    <li><span class="thumb" role="img" aria-label="Photo of a student in a prayer pose" style="background:linear-gradient(#f1ede8,#b39a86)"></span><div><p>Lorem ipsum dolor sit amet, consectetur adipiscing elit.</p><div class="stats"><span>654 <svg width="14" height="12"><path d="M7 11L1 5a3 3 0 015-3l1 1 1-1a3 3 0 015 3z" fill="#333"/></svg></span><span>352 <svg width="16" height="10"><ellipse cx="8" cy="5" rx="7.5" ry="4.5" fill="#333"/><circle cx="8" cy="5" r="2" fill="#fff"/></svg></span></div></div></li>
    <li><span class="thumb" role="img" aria-label="Photo of a student in a seated stretch" style="background:linear-gradient(#f4f2ee,#c9b29a 70%,#7a4a8a)"></span><div><p>Lorem ipsum dolor sit amet, consectetur adipiscing elit.</p><div class="stats"><span>654 <svg width="14" height="12"><path d="M7 11L1 5a3 3 0 015-3l1 1 1-1a3 3 0 015 3z" fill="#333"/></svg></span><span>352 <svg width="16" height="10"><ellipse cx="8" cy="5" rx="7.5" ry="4.5" fill="#333"/><circle cx="8" cy="5" r="2" fill="#fff"/></svg></span></div></div></li>
    <li><span class="thumb" role="img" aria-label="Photo of a student in a side plank pose" style="background:linear-gradient(#f7f7f7,#d8d8d8 60%,#3a3a3a)"></span><div><p>Lorem ipsum dolor sit amet, consectetur adipiscing elit.</p><div class="stats"><span>654 <svg width="14" height="12"><path d="M7 11L1 5a3 3 0 015-3l1 1 1-1a3 3 0 015 3z" fill="#333"/></svg></span><span>352 <svg width="16" height="10"><ellipse cx="8" cy="5" rx="7.5" ry="4.5" fill="#333"/><circle cx="8" cy="5" r="2" fill="#fff"/></svg></span></div></div></li>
    <li><span class="thumb" role="img" aria-label="Photo of a student meditating" style="background:linear-gradient(#6fa6d8,#2f6fb3)"></span><div><p>Lorem ipsum dolor sit amet, consectetur adipiscing elit.</p><div class="stats"><span>654 <svg width="14" height="12"><path d="M7 11L1 5a3 3 0 015-3l1 1 1-1a3 3 0 015 3z" fill="#333"/></svg></span><span>352 <svg width="16" height="10"><ellipse cx="8" cy="5" rx="7.5" ry="4.5" fill="#333"/><circle cx="8" cy="5" r="2" fill="#fff"/></svg></span></div></div></li>
  </ul>

  <div class="abs band"></div>
  <a class="abs band-btn">REQUEST A QOUTE</a>
  <div class="abs band-social">
    <span></span>
    <span></span>
    <span><svg width="12" height="12" viewBox="0 0 12 12"><circle cx="2" cy="10" r="1.6" fill="#9a9a9a"/><path d="M1 5.5a5.5 5.5 0 015.5 5.5M1 1.5a9.5 9.5 0 019.5 9.5" stroke="#9a9a9a" stroke-width="1.8" fill="none"/></svg></span>
    <span><svg width="12" height="12" viewBox="0 0 12 12"><path d="M6 1v10M1 6h10" stroke="#9a9a9a" stroke-width="2.4"/></svg></span>
  </div>

  <footer class="abs footer"></footer>
  <div class="abs corner"></div>
  <div class="abs fcol" style="left:141px"><h3>Customer Service</h3><ul><li>Introduction</li><li>Request An Appointment</li><li>Place A New Order</li><li>Send A File</li><li>Document Library</li></ul></div>
  <div class="abs fcol" style="left:399px"><h3>Resources</h3><ul><li>Introduction</li><li>FAQ's</li><li>Glossary of Terms</li><li>Excellart Videos</li></ul></div>
  <div class="abs fcol" style="left:631px"><h3>About Us</h3><ul><li>Company Culture</li><li>Our Staff</li><li>Departments</li><li>Employement Opportunities</li><li>Location &amp; Hours</li></ul></div>
  <div class="abs fcol" style="left:865px"><h3>Contact Us</h3>
    <div class="addr"><svg width="11" height="16" viewBox="0 0 11 16" style="margin-top:3px"><path d="M5.5 0a5.5 5.5 0 015.5 5.5C11 9 5.5 16 5.5 16S0 9 0 5.5A5.5 5.5 0 015.5 0z" fill="#888"/><circle cx="5.5" cy="5.5" r="2" fill="#232323"/></svg><span>107 Lorem ipsum dolor sit amet<br>Street : 1234 consectetur adip<br>sicing elit..</span></div>
    <div class="addr" style="margin-top:9px"><svg width="11" height="16" viewBox="0 0 11 16" style="margin-top:3px"><rect x="0.75" y="0.75" width="9.5" height="14.5" rx="1.5" fill="none" stroke="#888" stroke-width="1.5"/><rect x="3" y="12" width="5" height="1.5" fill="#888"/></svg><span>0800-555-0142</span></div>
  </div>
  <div class="abs base">Copyrights © 2015 Mirel - All Rights Reserved</div>
</div>
</div>
</body>
</html>
```